Rulo Bristow

I need a design for a packaging box containing a eyebrow and eyelash lamination kit. The size of the outer box is 11.7 long x 7.9 wide x 3.2 cm high. The design needs to have the attached brand logo and the following 'Eyebrow and Eyelash Luxury Lamination Kit'

Target Market(s)

e-commerce

Font styles to use
Script

```html
<!DOCTYPE html>
<html lang="en">
<head>
<meta charset="utf-8">
<title>Rulo Bristow – Lamination Kit Box</title>
<link href="https://fonts.googleapis.com/css2?family=Playfair+Display:wght@400;500&display=swap" rel="stylesheet">
<style>
  :root {
    --backdrop: #e6e4e5;
    --silver-light: #f2f2f2;
    --silver-mid: #c9c9c9;
    --silver-dark: #8d8d8d;
    --ink: #1b1b1c;
    --ink-soft: #2c2c2e;
    --ink-sheen: #4a4a4c;
    --band: #232325;
    --gold: #c9a24a;
    --white: #f4f4f4;
  }
  * { margin: 0; padding: 0; box-sizing: border-box; }
  html, body { width: 1200px; height: 840px; overflow: hidden; background: var(--backdrop); }
  .canvas { position: relative; width: 1200px; height: 840px; }

  .dark-texture {
    background: linear-gradient(160deg, var(--ink-soft) 0%, var(--ink) 35%, var(--ink-sheen) 52%, var(--ink) 68%, var(--ink-soft) 100%);
  }

  /* Top face */
  .lid {
    position: absolute; left: 346px; top: 88px; width: 700px; height: 473px;
    overflow: hidden; box-shadow: 0 6px 20px rgba(0,0,0,.10);
  }
  .lid-texture {
    position: absolute; inset: 0;
    background: linear-gradient(100deg, var(--silver-mid) 0%, var(--silver-light) 22%, var(--silver-dark) 40%, var(--silver-light) 58%, var(--silver-mid) 78%, var(--silver-light) 100%);
  }
  .brand-band {
    position: absolute; left: 0; right: 0; top: 200px; height: 68px;
    background: var(--band);
    display: flex; align-items: center; justify-content: flex-end; padding-right: 60px;
  }
  .brand-lockup { display: flex; align-items: center; gap: 18px; }
  .brand-mark { width: 10px; height: 10px; border-radius: 50%; background: var(--gold); }
  .brand-divider { width: 2px; height: 42px; background: var(--gold); }
  .brand-name {
    font-family: "Playfair Display", serif; font-weight: 400; font-variant: small-caps;
    font-size: 38px; letter-spacing: 2px; color: var(--gold); line-height: 1; white-space: nowrap;
  }
  .title-panel {
    position: absolute; left: 50px; top: 50px; width: 212px; height: 373px;
    border: 2px solid var(--gold);
    display: flex; flex-direction: column; align-items: center; justify-content: center;
    text-align: center; font-family: "Playfair Display", serif;
  }
  .title-main { color: var(--white); font-size: 36px; line-height: 1.05; font-weight: 400; }
  .title-joiner { color: var(--white); font-size: 13px; display: block; margin: 3px 0; }
  .title-sub { color: var(--gold); font-size: 21px; line-height: 1.15; margin-top: 18px; }

  /* Short end panel */
  .end-panel {
    position: absolute; left: 155px; top: 88px; width: 191px; height: 473px; overflow: hidden;
  }
  .end-content {
    position: absolute; left: 50%; top: 50%; width: 473px; height: 191px;
    transform: translate(-50%, -50%) rotate(-90deg);
    display: flex; flex-direction: column; align-items: center; justify-content: center;
    text-align: center; font-family: "Playfair Display", serif;
  }
  .end-title { color: var(--white); font-size: 32px; line-height: 1; font-weight: 400; }
  .end-title .title-joiner { font-size: 12px; margin: 2px 0; }
  .end-sub { color: var(--gold); font-size: 17px; letter-spacing: 5px; margin-top: 12px; line-height: 1.2; }

  /* Long front panel */
  .front-panel {
    position: absolute; left: 346px; top: 561px; width: 700px; height: 191px; overflow: hidden;
  }
  .front-frame {
    position: absolute; left: 80px; right: 40px; top: 34px; bottom: 34px;
    border: 1px solid var(--gold);
    display: flex; align-items: center; justify-content: center;
  }
</style>
</head>
<body>
<main class="canvas">
  <section class="end-panel dark-texture">
    <div class="end-content">
      <p class="end-title">Eyebrow<span class="title-joiner">and</span>Eyelash</p>
      <p class="end-sub">Luxury Lamination Kit</p>
    </div>
  </section>

  <section class="lid">
    <div class="lid-texture" role="img" aria-label="Brushed silver hair-like texture"></div>
    <div class="brand-band">
      <div class="brand-lockup">
        <span class="brand-mark"></span>
        <span class="brand-divider"></span>
        <span class="brand-name">Rulo Bristow</span>
      </div>
    </div>
    <div class="title-panel dark-texture">
      <h1 class="title-main">Eyebrow<span class="title-joiner">and</span>Eyelash</h1>
      <p class="title-sub">Luxury Lamination<br>Kit</p>
    </div>
  </section>

  <section class="front-panel dark-texture">
    <div class="front-frame">
      <div class="brand-lockup">
        <span class="brand-mark"></span>
        <span class="brand-divider"></span>
        <span class="brand-name">Rulo Bristow</span>
      </div>
    </div>
  </section>
</main>
</body>
</html>
```